Hula-Hoop dance entertainment sales and instruction by spin-wisp needs a business card

I need a 2 sided business card that is square (although this is not an absolute )for my self employed business as an independent artist. my business name is "Spin-Wisp" I teach how to hula-hoop classes, make and sell hula-hoops, provided entertainment at kids birthday parties, community events, corporate events and perform at artistic dance shows.
I would like to see spirals or curved lines in the card, and I would like the card to be seen as fun, spunky, flair and eye catching.

the card could double as a tag to go on the hoops i sell,

Target Market(s)

women age 20 - 50

Industry/Entity Type

Entertainment

Requirements
Must have
• Dena Marwick
www.spinwispdemo.com
555.014.7263
Nice to have
• I would like my image to be on one side of the card. so people can recognize me!

```html
<!DOCTYPE html>
<html lang="en">
<head>
<meta charset="utf-8">
<title>Spin Wisp – Business Card</title>
<link rel="stylesheet" href="https://fonts.googleapis.com/css2?family=Architects+Daughter&display=swap">
<style>
  :root {
    --magenta: #c2489a;
    --blush: #fbe3ef;
    --sky-ink: #1f7bc8;
    --ink: #1a1a1a;
    --lilac: #b68bc3;
    --mint: #7ec688;
    --tangerine: #f5a01e;
    --cornflower: #6d97cd;
    --powder: #a9cdeb;
    --lime: #acd78a;
    --periwinkle: #9b8fc8;
    --white: #ffffff;
  }
  * { margin: 0; padding: 0; box-sizing: border-box; }
  html, body {
    width: 1200px;
    height: 2500px;
    overflow: hidden;
    background: var(--white);
  }
  .card {
    position: absolute;
    left: 0;
    width: 1200px;
    overflow: hidden;
    background: var(--magenta);
    font-family: "Architects Daughter", cursive;
  }
  .card--front { top: 0; height: 1180px; }
  .card--back { top: 1325px; height: 1175px; }
  .card__shapes {
    position: absolute;
    inset: 0;
    width: 100%;
    height: 100%;
  }
  .brand-name {
    position: absolute;
    margin: 0;
    font-weight: 400;
    line-height: 1;
    white-space: nowrap;
  }
  .card--front .brand-name {
    left: 70px;
    top: 80px;
    font-size: 215px;
    line-height: 0.95;
    color: var(--sky-ink);
  }
  .card--back .brand-name {
    left: 470px;
    top: 150px;
    font-size: 150px;
    color: var(--ink);
  }
  .art-slot {
    position: absolute;
    left: 312px;
    top: 562px;
    width: 668px;
    height: 584px;
    background: linear-gradient(180deg, #f4dbe8 0%, #e9d1de 60%, #d9c3d0 100%);
    border-radius: 12px;
  }
  .contact {
    position: absolute;
    left: 177px;
    top: 440px;
    color: var(--ink);
  }
  .contact__name {
    font-size: 76px;
    line-height: 1;
    letter-spacing: 2px;
    margin-bottom: 20px;
  }
  .contact__line {
    font-size: 60px;
    line-height: 1.35;
    letter-spacing: 1px;
  }
  .portrait-slot {
    position: absolute;
    left: 396px;
    top: 715px;
    width: 739px;
    height: 440px;
    border-radius: 40px;
    background: linear-gradient(160deg, #c9826a 0%, #e5bfa8 40%, #3f9d9a 75%, #c7c7cf 100%);
  }
</style>
</head>
<body>

<section class="card card--front" aria-label="Card front">
  <svg class="card__shapes" viewBox="0 0 1200 1180" aria-hidden="true">
    <path fill="var(--blush)" d="M0 0 L560 0 C 780 20 1010 70 1110 300 C 1170 440 1190 650 1200 830 L1200 1180 L0 1180 Z"/>
    <circle cx="621" cy="142" r="98" fill="var(--lilac)"/>
    <circle cx="1042" cy="344" r="156" fill="var(--mint)"/>
    <circle cx="31" cy="615" r="73" fill="var(--tangerine)"/>
    <circle cx="94" cy="1052" r="125" fill="var(--cornflower)"/>
  </svg>
  <h1 class="brand-name">Spin<br>Wisp</h1>
  <div class="art-slot" role="img" aria-label="Ink illustration of two flapper-style women, one standing with a hoop at her feet and one spinning a hula hoop"></div>
</section>

<section class="card card--back" aria-label="Card back">
  <svg class="card__shapes" viewBox="0 0 1200 1175" aria-hidden="true">
    <path fill="var(--blush)" d="M0 529 C 90 300 420 110 1200 22 L1200 1175 L0 1175 Z"/>
    <circle cx="267" cy="279" r="110" fill="var(--powder)"/>
    <circle cx="1092" cy="425" r="108" fill="var(--lime)"/>
    <circle cx="62" cy="935" r="135" fill="var(--periwinkle)"/>
  </svg>
  <h2 class="brand-name">Spin Wisp</h2>
  <div class="contact">
    <p class="contact__name">Dena Marwick</p>
    <p class="contact__line">www.spinwispdemo.com</p>
    <p class="contact__line">555.014.7263</p>
  </div>
  <div class="portrait-slot" role="img" aria-label="Photo of the performer holding a teal hula hoop around her shoulders"></div>
</section>

</body>
</html>
```